Packaging design for a Deli Shop "TORVO Gourmet"

We need a packaging design for a new Deli Business we are opening soon. We produce food to be packaged and sold either fresh or frozen in transparent disposable plastic boxes, cardboard boxes and finally delivered in a bag (Paper, plastic or shopping bag whatever goes best with the design) to take out. The food we generally pack are salads, lasagnas, ceviches, sandwiches, cookies, granola, dips, etc.

The name of the company is "TORVO Gourmet" Check our website for reference: www.torvogourmet-example.com

We have a logo and a name we want to maintain (attached).

The product will be sold in our new deli store, that is inspired in big cities delikatessen, quite modern and trendy. It also delivers a message that everything we sell is high quality, artisan (not massive or mainstream) and great in flavors.

Packaging must communicate freshness, great flavor, high quality and high price.

Packaging must be feasible to produce and print easily without any complex or impossible to implement packaging, (preferrable to be done or easy to adapt from generic packaging).

All our communication will be in Spanish so please do not depend on english for the design. If english or any other language is used, please be sure its understandable in almost any country (ie Basic English, Italian).

Same packaging (labeling or boxes and bags) will be used, just changing the name of the product inside according to the product.

Most of our product will be displayed in refrigerators and freezers.
Updates

I just uploaded a visual brief of the packaging examples we would like to have.

Looking forward to see your designs.
Thank you

Project Deadline Extended
Reason: Some designers who said will participate havent submitted their deaigns, and still what is being submitted is not fully complying with the requirements. Thank you

Target Market(s)

The main target is High SEL, between 24 and 40, mostly woman

Industry/Entity Type

Communication

Requirements
Must have

Nice to have
• Please take a look at my website www.torvogourmet-example.com to see the kind of coloring we are aiming to have.

Give the impression of being "Green"...

Include "Kraft" color paper / Brown paper color
Should not have
• Complex packaging difficult to implement in a simple print shop.
Expensive items.

```html
<!DOCTYPE html>
<html lang="es">
<head>
<meta charset="utf-8">
<title>TORVO Gourmet — cintillos</title>
<link rel="stylesheet" href="https://fonts.googleapis.com/css2?family=Quicksand:wght@400;500&family=Raleway:wght@300&family=Nothing+You+Could+Do&display=swap">
<style>
  :root {
    --paper: #ffffff;
    --kraft: #e4c5ab;
    --label-grey: #6e6e6e;
    --salad-green: #8cfc14;
    --salad-lime: #bfff0a;
    --salad-soft: #cbf51e;
    --salad-script: #86c820;
    --dessert-violet: #8000ff;
    --dessert-magenta: #c400ff;
    --dessert-pink: #c21fe3;
    --dessert-plum: #5a0fa3;
    --dessert-blue: #8a12f2;
    --dessert-script: #6a00c0;
    --cream: #fbf4ee;
    --white: #ffffff;
  }
  * { margin: 0; padding: 0; box-sizing: border-box; }
  html, body { width: 763px; height: 1200px; overflow: hidden; background: var(--paper); }
  .sheet { display: block; width: 763px; height: 1200px; }
  .section-title { font-family: 'Raleway', sans-serif; font-weight: 300; font-size: 32px; fill: var(--label-grey); }
  .kraft { fill: var(--kraft); }
  .brand { font-family: 'Quicksand', sans-serif; font-weight: 500; fill: var(--white); }
  .product { font-family: 'Quicksand', sans-serif; font-weight: 400; fill: var(--white); }
  .category { font-family: 'Nothing You Could Do', cursive; }
  .category--salad { fill: var(--salad-script); }
  .category--dessert { fill: var(--dessert-script); }
</style>
</head>
<body>
<svg class="sheet" viewBox="0 0 763 1200" xmlns="http://www.w3.org/2000/svg">
  <defs>
    <clipPath id="salad-band-clip"><rect x="247" y="70" width="194" height="686"/></clipPath>
    <clipPath id="salad-seal-clip"><circle cx="357" cy="410" r="222"/></clipPath>
    <clipPath id="dessert-seal-clip"><circle cx="495" cy="1024" r="152"/></clipPath>
  </defs>

  <!-- Cintillo ensalada -->
  <g class="band band--salad">
    <text class="section-title" x="214" y="48">cintillo ensalada</text>
    <rect class="kraft" x="247" y="70" width="194" height="686"/>
    <g clip-path="url(#salad-band-clip)">
      <circle role="img" aria-label="Círculo con hoja dibujada" cx="296" cy="98" r="43" fill="var(--salad-soft)"/>
      <circle role="img" aria-label="Círculo con hoja dibujada" cx="414" cy="98" r="32" fill="var(--salad-soft)"/>
      <circle role="img" aria-label="Círculo con hoja dibujada" cx="373" cy="148" r="28" fill="var(--salad-green)"/>
      <circle role="img" aria-label="Círculo con hoja dibujada" cx="299" cy="690" r="52" fill="var(--salad-green)"/>
      <circle role="img" aria-label="Círculo con hoja dibujada" cx="416" cy="690" r="32" fill="var(--salad-soft)"/>
    </g>
    <g clip-path="url(#salad-seal-clip)">
      <rect x="135" y="188" width="444" height="270" fill="var(--salad-green)"/>
      <rect x="135" y="458" width="444" height="174" fill="var(--salad-lime)"/>
    </g>
    <text class="brand" x="352" y="372" font-size="96" text-anchor="middle">TORVO</text>
    <text class="brand" x="352" y="430" font-size="34" letter-spacing="13" text-anchor="middle">GOURMET</text>
    <text class="category category--salad" x="357" y="500" font-size="38" text-anchor="middle">ensaladas</text>
    <text class="product" x="362" y="546" font-size="28" text-anchor="middle">Risoni Mediterranea</text>
  </g>

  <!-- Cintillo postres -->
  <g class="band band--dessert">
    <text class="section-title" x="150" y="868">cintillo postres</text>
    <rect class="kraft" x="32" y="944" width="687" height="193"/>
    <circle role="img" aria-label="Círculo decorativo de puntos" cx="93" cy="1010" r="55" fill="var(--dessert-pink)"/>
    <circle role="img" aria-label="Círculo decorativo de puntos" cx="207" cy="988" r="28" fill="var(--cream)"/>
    <circle role="img" aria-label="Círculo decorativo de puntos" cx="291" cy="1035" r="28" fill="var(--dessert-pink)"/>
    <circle role="img" aria-label="Círculo decorativo de puntos" cx="205" cy="1090" r="38" fill="var(--dessert-plum)"/>
    <circle role="img" aria-label="Círculo decorativo de puntos" cx="677" cy="995" r="22" fill="var(--cream)"/>
    <circle role="img" aria-label="Círculo decorativo de puntos" cx="680" cy="1103" r="30" fill="var(--dessert-blue)"/>
    <g clip-path="url(#dessert-seal-clip)">
      <rect x="343" y="872" width="304" height="183" fill="var(--dessert-violet)"/>
      <rect x="343" y="1055" width="304" height="121" fill="var(--dessert-magenta)"/>
    </g>
    <text class="brand" x="490" y="1008" font-size="64" text-anchor="middle">TORVO</text>
    <text class="brand" x="490" y="1040" font-size="23" letter-spacing="9" text-anchor="middle">GOURMET</text>
    <text class="category category--dessert" x="480" y="1090" font-size="32" text-anchor="middle">postres</text>
    <text class="product" x="487" y="1122" font-size="17" text-anchor="middle">brownies</text>
  </g>
</svg>
</body>
</html>
```